Website for Verdix Partners

We need to create a website for our company. Attached is the site map of the website and data input needed. Our theme colour is RED and our Logo is attached

We need a very attractive design where graphics are largely used like flash.

The main idea of the website is to show Telecommunications Suppliers World Wide that we could assist them in getting more business in Africa and Middle East through our local presence in this region.

Target Market(s)

Telecommunication Suppliers and Clients

Industry/Entity Type

Business

Font styles to use
Serif
Sans Serif

Colors
ec2027

Requirements
Must have
• Graphics that shows Telecommunications Suppliers World Wide that we could assist them in getting more business in Africa and Middle East through our local presence in this region.

The website should be easy to edit for future changes by us.
Nice to have
• New ideas

```html
<!DOCTYPE html>
<html lang="en">
<head>
<meta charset="utf-8">
<title>Verdix Partners</title>
<link href="https://fonts.googleapis.com/css2?family=Pathway+Gothic+One&family=Jost:wght@400;500&family=Montserrat:wght@600&display=swap" rel="stylesheet">
<style>
  :root {
    --brand-red: #ec2027;
    --ink: #222222;
    --nav-grey: #5d6670;
    --panel-grey: #e5e6e5;
    --field-green: #9dc31c;
    --footer-bg: #232529;
    --footer-ink: #e4e4e4;
    --sky-light: #cfe0f1;
    --sky-mid: #7fb0de;
    --sky-deep: #3a88cf;
    --dish-white: #f3efe6;
    --mast-steel: #6e6a62;
    --mast-red: #c9473f;
    --heading-font: "Pathway Gothic One", "Arial Narrow", sans-serif;
    --body-font: Arial, Helvetica, sans-serif;
    --ui-font: "Jost", Arial, sans-serif;
    --brand-font: "Montserrat", Arial, sans-serif;
  }
  * { margin: 0; padding: 0; box-sizing: border-box; }
  html, body { width: 1200px; height: 1099px; overflow: hidden; background: #fff; }
  body { position: relative; font-family: var(--body-font); color: var(--ink); }

  .social-links { position: absolute; left: 683px; top: 16px; display: flex; gap: 8px; }
  .social-links span { width: 24px; height: 24px; background: var(--nav-grey); display: block; }

  .contact-line { position: absolute; left: 787px; top: 17px; font-family: var(--heading-font); font-size: 16px; color: var(--brand-red); white-space: nowrap; }
  .contact-line .divider { margin: 0 8px; }

  .brand { position: absolute; left: 208px; top: 63px; display: flex; align-items: center; gap: 14px; }
  .brand-square { width: 40px; height: 40px; background: var(--brand-red); }
  .brand-name { font-family: var(--brand-font); font-weight: 600; font-size: 31px; letter-spacing: 1px; color: var(--nav-grey); }

  .main-nav { position: absolute; left: 652px; top: 82px; display: flex; gap: 17px; }
  .main-nav a { font-family: var(--heading-font); font-size: 20px; color: var(--nav-grey); text-decoration: none; text-transform: uppercase; }

  .hero { position: absolute; left: 0; top: 145px; width: 1200px; height: 364px;
    background:
      radial-gradient(ellipse 330px 260px at 300px 210px, rgba(243,239,230,.95) 0%, rgba(243,239,230,.55) 45%, rgba(243,239,230,0) 100%),
      radial-gradient(ellipse 240px 170px at 420px 300px, rgba(110,106,98,.45) 0%, rgba(110,106,98,0) 100%),
      radial-gradient(ellipse 110px 260px at 920px 260px, rgba(201,71,63,.5) 0%, rgba(201,71,63,0) 100%),
      linear-gradient(100deg, var(--sky-light) 0%, var(--sky-mid) 45%, var(--sky-deep) 100%); }
  .hero-dot { position: absolute; left: 983px; top: 335px; width: 11px; height: 11px; border-radius: 50%; background: #111; }

  .about { position: absolute; left: 184px; top: 554px; width: 570px; }
  .section-title { font-family: var(--heading-font); font-size: 27px; color: var(--ink); font-weight: 400; }
  .about p { font-size: 10.5px; line-height: 17px; margin-top: 12px; }
  .about h3 { font-size: 11.5px; font-weight: bold; margin-top: 17px; letter-spacing: .4px; }
  .about h3 + p { margin-top: 1px; }

  .service-photo { position: absolute; top: 701px; width: 211px; height: 140px; }
  .photo-network { left: 184px; background: linear-gradient(135deg, #cfd3d7 0%, #9aa1a7 50%, #2f86c9 100%); }
  .photo-phones { left: 466px; background: linear-gradient(180deg, #f2f2f2 0%, #8a8f94 55%, #4d5a86 100%); }

  .service { position: absolute; top: 867px; }
  .service-network { left: 173px; width: 261px; }
  .service-managed { left: 466px; width: 290px; }
  .service p { font-size: 10.1px; line-height: 17px; text-align: justify; margin-top: 6px; }

  .newsletter { position: absolute; left: 789px; top: 550px; width: 288px; height: 291px; background: var(--panel-grey); border-radius: 3px; padding: 20px 10px 20px 25px; }
  .newsletter p { font-family: var(--ui-font); font-size: 12px; line-height: 18.5px; margin-top: 6px; color: #333; letter-spacing: .2px; }
  .field { display: block; width: 186px; height: 41px; border: 2px solid var(--field-green); background: #fff; margin-top: 10px; padding: 0 14px; font-family: var(--body-font); font-size: 14px; color: #9a9a9a; line-height: 37px; }
  .newsletter .field:first-of-type { margin-top: 19px; }
  .login-button { display: block; margin-top: 15px; width: 98px; height: 33px; background: var(--brand-red); color: #fff; border-radius: 3px; font-family: var(--ui-font); font-weight: 500; font-size: 17px; line-height: 33px; padding-left: 26px; }

  .site-footer { position: absolute; left: 0; top: 1053px; width: 1200px; height: 46px; background: var(--footer-bg); border-top: 2px solid #000; text-align: center; font-size: 10.5px; line-height: 42px; color: var(--footer-ink); }
</style>
</head>
<body>
  <div class="social-links" aria-label="Social links"><span></span><span></span><span></span></div>
  <div class="contact-line">024 318 650<span class="divider">|</span>hello@verdix-partners.com</div>

  <div class="brand"><span class="brand-square"></span><span class="brand-name">VERDIX PARTNERS</span></div>

  <nav class="main-nav">
    <a href="#">Home</a><a href="#">Company</a><a href="#">Portfolio</a><a href="#">Footprint</a><a href="#">Contact</a>
  </nav>

  <div class="hero" role="img" aria-label="Telecommunication towers with white dish antennas and a red and white mast against a blue sky">
    <span class="hero-dot"></span>
  </div>

  <section class="about">
    <h2 class="section-title">About Verdix Partners</h2>
    <p>Verdix Partners is a leading telecommunication Solution Provider; the company provides state of the art technologies and turnkey solutions to its clients that fully support their business needs from planning right through full operation</p>
    <h3>We Serve you Everywhere</h3>
    <p>Our Head office in UK and we cover Middle East and Africa thorough a large and strong group of local footprint.</p>
  </section>

  <div class="service-photo photo-network" role="img" aria-label="Hand plugging a blue network cable into a switch"></div>
  <div class="service-photo photo-phones" role="img" aria-label="Office desk phones on top of a network switch"></div>

  <section class="service service-network">
    <h2 class="section-title">Access Network Solutions</h2>
    <p>Lorem ipsum dolor sit amet, consectetur adipiscing elit. Sed at ante. Mauris eleifend, quam a vulputate dictum, massa quam dapibus leo, eget vulputate orci purus ut lorem. In fringilla mi in ligula. Pellentesque aliquam quam vel dolor. Nunc adipiscing. Sed quam odio,</p>
  </section>

  <section class="service service-managed">
    <h2 class="section-title">Managed Services</h2>
    <p>Lorem ipsum dolor sit amet, consectetur adipiscing elit. Sed at ante. Mauris eleifend, quam a vulputate dictum, massa quam dapibus leo, eget vulputate orci purus ut lorem. In fringilla mi in ligula. Pellentesque aliquam quam vel dolor. Nunc adipiscing. Sed quam odio, tempus ac, aliquam molestie, varius ac, tellus.</p>
  </section>

  <aside class="newsletter">
    <h2 class="section-title">Register for Newsletter</h2>
    <p>Lorem ipsum dolor sit amet, consectetur adipisicing elit, sed do eiusmod tempor incididunt ut labore et dolore magna aliqua.</p>
    <span class="field">Username</span>
    <span class="field">Password</span>
    <span class="login-button">Login</span>
  </aside>

  <footer class="site-footer">Copyright 2014 Verdix Partners - Terms &amp; Conditions | Privacy Policy</footer>
</body>
</html>
```